Flyer-Design für Unkrautbekämpfung
Zielgruppe
Unkrautbekämpfung mit dem Heißwasser-Schaum-System. In Eigenleistung und Vermietung des Geräts.
Zielgruppe: Privatleute mit eigenem Grundstück, Landwirte, kleine Geschäfte (Restaurants, Läden mit Parkplatz etc.)
Aufgabenstellung
Link zur Website: www.beetklar-service.net
Der Kreativität sind keine Grenzen gesetzt.
Bitte Vorder- und Rückseite designen. Auf der Rückseite können hauptsächlich Kontaktinformationen sein.

```html
<!DOCTYPE html>
<html lang="de">
<head>
<meta charset="utf-8">
<title>BKS Flyer – Vorder- und Rückseite</title>
<link rel="stylesheet" href="https://fonts.googleapis.com/css2?family=Source+Sans+3:wght@400;600;700&display=swap">
<style>
  :root {
    --green: #2e7d3a;
    --green-dark: #256b30;
    --navy: #1f2a5a;
    --ink: #1c1c1c;
    --paper: #ffffff;
    --stage: #f3f3f1;
  }
  * { box-sizing: border-box; margin: 0; padding: 0; }
  html, body { width: 1200px; height: 846px; overflow: hidden; }
  body {
    background: var(--stage);
    font-family: "Source Sans 3", Arial, sans-serif;
    color: var(--ink);
    position: relative;
  }
  .flyer {
    position: absolute;
    top: 41px;
    width: 540px;
    height: 764px;
    background: var(--paper);
    overflow: hidden;
    box-shadow: 0 2px 10px rgba(0,0,0,.12);
  }
  .flyer--front { left: 40px; }
  .flyer--back { left: 620px; }

  /* brand */
  .brand { position: absolute; left: 52px; top: 38px; display: flex; align-items: center; gap: 12px; }
  .brand__mark { width: 40px; height: 40px; background: var(--green); }
  .brand__name { color: var(--green); font-weight: 600; font-size: 24px; line-height: 1; }
  .brand__line { color: var(--green); font-weight: 600; font-size: 15px; line-height: 1.2; margin-top: 3px; }

  .illustration-sprayer {
    position: absolute;
    background: linear-gradient(135deg, #cfe8cf 0%, #8fcb8f 55%, #2a2d5c 100%);
    opacity: .85;
  }
  .flyer--front .illustration-sprayer { right: 0; top: 20px; width: 175px; height: 110px; }
  .flyer--back .illustration-sprayer { right: 18px; top: 590px; width: 140px; height: 120px; }

  /* front */
  .hero-photo {
    position: absolute; left: 0; top: 120px; width: 540px; height: 400px;
    background: linear-gradient(160deg, #c9c9c9 0%, #8c9a6c 30%, #5f7d3e 55%, #7f8588 80%, #9a9ea6 100%);
  }
  .bubble { position: absolute; left: 215px; top: 130px; width: 190px; height: 175px; }
  .bubble__text {
    position: absolute; left: 20px; top: 18px;
    color: #fff; font-size: 27px; font-weight: 400; line-height: 1.12;
  }
  .benefits {
    position: absolute; left: 0; top: 520px; width: 540px; height: 185px;
    background: var(--green); color: #fff; text-align: center;
    padding-top: 22px;
  }
  .benefits__title { font-weight: 700; font-size: 19px; line-height: 1.2; }
  .benefits__list { list-style: none; margin-top: 16px; font-size: 17px; line-height: 1.7; }
  .benefits__list svg { width: 14px; height: 14px; margin-right: 6px; vertical-align: -1px; }
  .claims {
    position: absolute; left: 0; bottom: 0; width: 540px; height: 59px;
    display: flex; align-items: center; justify-content: center;
    color: var(--green); font-weight: 600; font-size: 13px;
  }

  /* back */
  .compare { position: absolute; left: 0; top: 130px; width: 540px; height: 340px; display: flex; }
  .compare__photo { position: relative; flex: 1; }
  .compare__photo--before { background: linear-gradient(180deg, #4f6f3a 0%, #7aa05a 45%, #9fae8e 75%, #8c9a80 100%); }
  .compare__photo--after { background: linear-gradient(180deg, #4a6a3a 0%, #8aa76a 40%, #c6c3bd 70%, #a8a6a2 100%); border-left: 3px solid #fff; }
  .compare__label {
    position: absolute; bottom: 24px; padding: 6px 22px;
    background: var(--green); color: #fff; font-weight: 600; font-size: 19px;
  }
  .compare__photo--before .compare__label { left: 20px; }
  .compare__photo--after .compare__label { left: 22px; }

  .contact-intro { position: absolute; left: 70px; top: 495px; width: 420px; color: var(--green); }
  .contact-intro__title { font-weight: 700; font-size: 28px; }
  .contact-intro__text { font-weight: 600; font-size: 15px; line-height: 1.25; margin-top: 4px; }
  .address { position: absolute; left: 70px; top: 605px; font-size: 15px; line-height: 1.3; }
  .address__name { font-weight: 700; }
  .address__lines { margin-top: 14px; }
  .address__lines svg { width: 13px; height: 13px; margin-right: 7px; vertical-align: -1px; fill: #9a9a9a; }
  .web-band {
    position: absolute; left: 0; bottom: 0; width: 540px; height: 44px;
    background: var(--green); color: #fff; font-weight: 600; font-size: 17px;
    display: flex; align-items: center; justify-content: center;
  }
</style>
</head>
<body>

<section class="flyer flyer--front" aria-label="Vorderseite">
  <div class="brand">
    <span class="brand__mark"></span>
    <div>
      <div class="brand__name">BKS</div>
      <div class="brand__line">Biologische Unkrautvernichtung</div>
    </div>
  </div>
  <div class="illustration-sprayer" role="img" aria-label="Illustration: Sprühgerät mit Schaum über grünem Unkraut"></div>

  <div class="hero-photo" role="img" aria-label="Foto: verunkrauteter Pflasterweg an einer Hauswand"></div>

  <svg class="bubble" viewBox="0 0 190 175" aria-hidden="true">
    <path d="M8 0 H182 a8 8 0 0 1 8 8 V170 L160 135 H8 a8 8 0 0 1 -8 -8 V8 a8 8 0 0 1 8 -8 Z" fill="#2e7d3a" stroke="#fff" stroke-width="2"/>
  </svg>
  <p class="bubble__text" style="left:235px;top:148px;">Unkraut<br>ohne Gift<br>im Griff</p>

  <div class="benefits">
    <h2 class="benefits__title">Flächenpflege mit dem Heißwasser-/<br>Ökoschaum-Verfahren</h2>
    <ul class="benefits__list">
      <li><svg viewBox="0 0 14 14"><path d="M1 7 L5 11 L13 2" fill="none" stroke="#fff" stroke-width="2"/></svg>Sofort sichtbares Ergebnis</li>
      <li><svg viewBox="0 0 14 14"><path d="M1 7 L5 11 L13 2" fill="none" stroke="#fff" stroke-width="2"/></svg>Geeignet für fast alle Untergründe</li>
      <li><svg viewBox="0 0 14 14"><path d="M1 7 L5 11 L13 2" fill="none" stroke="#fff" stroke-width="2"/></svg>Wirtschaftlich günstig</li>
    </ul>
  </div>
  <p class="claims">100% biologisch abbaubar • umweltfreundlich • nicht gesundheitsschädlich</p>
</section>

<section class="flyer flyer--back" aria-label="Rückseite">
  <div class="brand">
    <span class="brand__mark"></span>
    <div>
      <div class="brand__name">BKS</div>
      <div class="brand__line">Biologische Unkrautvernichtung</div>
    </div>
  </div>

  <div class="compare">
    <div class="compare__photo compare__photo--before" role="img" aria-label="Foto vorher: Tisch auf verunkrautetem Pflaster im Park">
      <span class="compare__label">vorher</span>
    </div>
    <div class="compare__photo compare__photo--after" role="img" aria-label="Foto nachher: Tisch auf sauberem Pflaster im Park">
      <span class="compare__label">nachher</span>
    </div>
  </div>

  <div class="contact-intro">
    <h2 class="contact-intro__title">Kontaktieren Sie uns!</h2>
    <p class="contact-intro__text">Gerne erarbeiten wir gemeinsam Ihr standortbezogenes Flächenpflegekonzept. Miete ist ebenfalls möglich.</p>
  </div>

  <address class="address" style="font-style:normal;">
    <div class="address__name">BKS - Biologische Unkrautvernichtung</div>
    <div>Lindenweg 14 • 29345 Sandhorst</div>
    <div class="address__lines">
      <div><svg viewBox="0 0 14 14"><path d="M3 1 L5.5 1 L6.5 4 L5 5.5 Q6.5 8.5 8.5 9 L10 7.5 L13 8.5 L13 11 Q12 13 10 13 Q2 11 1 3 Q1 1 3 1 Z"/></svg>Tel: 05081/4420 • Mobil: 0171/5528930</div>
      <div><svg viewBox="0 0 14 14"><path d="M0 3 H14 V12 H0 Z M0 3 L7 8 L14 3" /></svg>info@beetklar-service.net</div>
    </div>
  </address>

  <div class="illustration-sprayer" role="img" aria-label="Illustration: Sprühgerät mit Schaum über grünem Unkraut"></div>

  <div class="web-band">www.beetklar-service.net</div>
</section>

</body>
</html>
```